I own a small business whose primary function is Professional Fashion and Commercial Photography and has a secondary function of Talent Management of Models/Actors. I've used PrintaNova in the past to print my own design, but I'd like something a bit more topical, fresh and done by an artist instead of a photographer (me).

My company logo is included with a few selected horizontal (landscape) photos of some of my models--I'd like to use a single model photo as the background for the entire card, either in color or converted to black and white, at opacity enough to see the photo but not too much to obscure any text or the company logo, or use a photo as a share of the card (not the entire background), or use all the three models on the card in some manor... Our company colors are white, black, grey-silver and red.

Industry/Entity Type

Small Business

Contact Information for Business Card

Darnell Voskuijl, Owner
KLT Studios
PO Box 7316
Millbrook VT 05999-7316
(555) 014-2273
dan@kltstudios-example,.com

```html
<!DOCTYPE html>
<html lang="en">
<head>
<meta charset="utf-8">
<title>KLT Studios Business Card</title>
<link rel="stylesheet" href="https://fonts.googleapis.com/css2?family=Noto+Sans:wght@400;700&display=swap">
<style>
  :root {
    --bg: #e9e6e6;
    --black: #0b0b0b;
    --red: #e8141c;
    --red-deep: #a3080e;
    --grey: #5a5a5a;
    --silver: #8d8d8d;
    --white: #ffffff;
    --ink: #2b2b2b;
  }
  html, body {
    margin: 0;
    width: 1200px;
    height: 800px;
    overflow: hidden;
    background: var(--bg);
    font-family: "Noto Sans", Verdana, sans-serif;
  }
  .stage {
    position: relative;
    width: 1200px;
    height: 800px;
    display: flex;
    align-items: center;
    justify-content: center;
    gap: 50px;
  }
  .card {
    position: relative;
    width: 525px;
    height: 300px;
    overflow: hidden;
    box-shadow: 0 6px 18px rgba(0,0,0,0.25);
  }
  .card svg.card-art {
    position: absolute;
    inset: 0;
    width: 100%;
    height: 100%;
  }
  .card-back { background: var(--black); }
  .card-front { background: var(--red); }
  .model-photo {
    position: absolute;
    left: 230px;
    top: 70px;
    width: 295px;
    height: 230px;
    background: radial-gradient(ellipse at 65% 40%, #ff3a3f 0%, var(--red) 45%, var(--red-deep) 100%);
  }
  .brand-name { font-weight: 700; fill: var(--ink); }
  .person-name { fill: var(--white); font-size: 19px; }
  .person-title { fill: var(--red); font-size: 11px; }
  .contact-line { fill: var(--white); font-size: 14px; }
  .icon-box { fill: var(--red); }
  .icon-glyph { fill: none; stroke: var(--white); stroke-width: 1.4; }
</style>
</head>
<body>
<main class="stage">

  <section class="card card-back" aria-label="Business card, contact side">
    <svg class="card-art" viewBox="0 0 525 300" xmlns="http://www.w3.org/2000/svg">
      <path class="swoosh-red" fill="var(--red)" d="M262 0 C228 60 250 125 325 165 C390 200 400 250 380 300 L525 300 L525 0 Z"/>
      <path class="swoosh-black" fill="var(--black)" d="M278 0 C250 60 280 120 360 160 C420 190 440 230 430 300 L525 300 L525 0 Z"/>
      <path class="swoosh-grey" fill="var(--grey)" d="M285 0 C262 60 300 112 380 148 C440 174 490 185 525 190 L525 0 Z"/>
      <path class="swoosh-white" fill="var(--white)" d="M298 0 C275 55 312 103 392 134 C450 156 495 163 525 164 L525 0 Z"/>
      <line x1="320" y1="112" x2="520" y2="112" stroke="var(--red)" stroke-width="1"/>

      <rect class="brand-mark" x="330" y="55" width="26" height="26" fill="var(--red)"/>
      <text class="brand-name" x="364" y="77" font-size="24">KLT Studios</text>

      <text class="person-name" x="268" y="45" text-anchor="end">Darnell Voskuijl</text>
      <text class="person-title" x="140" y="60">Owner</text>

      <g class="contact-list">
        <rect class="icon-box" x="25" y="178" width="13" height="13" rx="3"/>
        <path class="icon-glyph" d="M28 185 L31.5 181.5 L35 185 M29 184.5 V189 H34 V184.5"/>
        <text class="contact-line" x="46" y="189">PO Box 7316 Millbrook VT 05999-7316</text>

        <rect class="icon-box" x="25" y="203" width="13" height="13" rx="3"/>
        <path class="icon-glyph" d="M29 206 C28 210 31 214 35 213"/>
        <text class="contact-line" x="46" y="214">(555) 014-2273</text>

        <rect class="icon-box" x="25" y="228" width="13" height="13" rx="3"/>
        <circle class="icon-glyph" cx="31.5" cy="234.5" r="3.5"/>
        <text class="contact-line" x="46" y="239">dan@kltstudios-example,.com</text>
      </g>
    </svg>
  </section>

  <section class="card card-front" aria-label="Business card, photo side">
    <div class="model-photo" role="img" aria-label="Photo of a studio model in a red sleeveless top reaching toward the camera against a red backdrop"></div>
    <svg class="card-art" viewBox="0 0 525 300" xmlns="http://www.w3.org/2000/svg">
      <path class="swoosh-black" fill="var(--black)" d="M0 62 C90 50 170 105 260 118 C340 128 400 95 430 0 L0 0 Z"/>
      <path class="swoosh-grey" fill="var(--grey)" d="M0 56 C90 42 170 96 260 108 C340 118 396 88 422 0 L0 0 Z"/>
      <path class="swoosh-white" fill="var(--white)" d="M0 46 C90 32 170 86 262 96 C338 104 388 76 410 0 L0 0 Z"/>
      <line x1="40" y1="68" x2="320" y2="68" stroke="var(--red)" stroke-width="1"/>

      <rect class="brand-mark" x="30" y="20" width="26" height="26" fill="var(--red)"/>
      <text class="brand-name" x="64" y="42" font-size="24">KLT Studios</text>
    </svg>
  </section>

</main>
</body>
</html>
```